Lantern Bay Dental Appointment Cards

This is a sister company of Marigold Dental Group
We are a returning client.
This is what we like:
We like Pemberly
Pemberly font is cool
our Client is mostly Hispanic
We like to put Dr. Okafor, WSPU Graduate
Please look at Marigold Dental Appt. Cards/Business Cards
Updates

We would like to see new logos, too.

Industry/Entity Type

Dental

Contact Information for Business Card

Tomas R. Okafor, D.D.S
WSPU Graduate
2847 West Linden Ave., Suite 310
Anaheim, CA 92806

Colors

Designer to choose colors to be used in the design.

Requirements
Nice to have
• Pemberly Features

```html
<!DOCTYPE html>
<html lang="en">
<head>
<meta charset="utf-8">
<title>Lantern Bay Dental – Appointment Card</title>
<link rel="stylesheet" href="https://fonts.googleapis.com/css2?family=Lato:wght@400;700&display=swap">
<style>
  :root {
    --backdrop: #3a3431;
    --card-dark: #111111;
    --card-light: #ffffff;
    --band: #222222;
    --accent-orange: #f39c12;
    --accent-blue: #2e8fd8;
    --text-light: #e8e8e8;
    --text-dark: #3a3a3a;
    --rule: #555555;
  }
  * { box-sizing: border-box; margin: 0; padding: 0; }
  html, body { width: 1200px; height: 900px; overflow: hidden; }
  body {
    background: var(--backdrop);
    font-family: "Lato", sans-serif;
    display: flex;
    align-items: center;
    justify-content: center;
    gap: 40px;
  }
  .card {
    width: 540px;
    height: 309px;
    position: relative;
    box-shadow: 0 10px 30px rgba(0,0,0,.45);
  }

  /* Front */
  .card-front {
    background: var(--card-dark);
    display: flex;
    align-items: center;
  }
  .brand {
    width: 270px;
    display: flex;
    flex-direction: column;
    align-items: center;
    gap: 14px;
  }
  .brand-mark {
    width: 58px; height: 58px;
    border: 3px solid var(--accent-orange);
    border-radius: 50%;
  }
  .brand-name {
    color: var(--accent-orange);
    font-weight: 700;
    font-size: 24px;
    letter-spacing: .5px;
    text-transform: uppercase;
  }
  .divider {
    width: 1px;
    height: 150px;
    background: var(--rule);
  }
  .contact {
    padding-left: 26px;
    color: var(--text-light);
    font-size: 15px;
    line-height: 1.35;
  }
  .doctor-name {
    color: var(--accent-orange);
    font-weight: 700;
    font-size: 16px;
    text-transform: uppercase;
  }
  .phone {
    display: flex;
    align-items: center;
    gap: 8px;
    margin: 12px 0 14px;
  }
  .phone svg { width: 16px; height: 16px; }

  /* Back */
  .card-back {
    background: var(--card-light);
    display: flex;
    flex-direction: column;
  }
  .appointment {
    padding: 44px 34px 0;
    color: var(--text-dark);
    flex: 1;
  }
  .appointment-line {
    font-weight: 700;
    font-size: 15px;
    letter-spacing: .3px;
  }
  .appointment-line .fill {
    font-weight: 400;
    font-size: 13px;
    color: #666;
  }
  .days {
    display: flex;
    justify-content: space-between;
    margin-top: 34px;
    font-size: 14px;
    color: #555;
  }
  .day { display: flex; align-items: center; gap: 5px; }
  .day-box {
    width: 16px; height: 16px;
    border: 1.5px solid #777;
  }
  .notice-band {
    background: var(--band);
    color: #f2f2f2;
    text-align: center;
    font-size: 14px;
    padding: 14px 0;
  }
  .website {
    text-align: center;
    font-size: 14px;
    padding: 14px 0 18px;
    color: var(--accent-blue);
  }
  .website .domain { color: var(--accent-orange); }
</style>
</head>
<body>

  <section class="card card-front">
    <div class="brand">
      <div class="brand-mark"></div>
      <div class="brand-name">Lantern Bay Dental</div>
    </div>
    <div class="divider"></div>
    <div class="contact">
      <div class="doctor-name">Tomas R. Okafor, D.D.S</div>
      <div>WSPU Graduate</div>
      <div class="phone">
        <svg viewBox="0 0 16 16" aria-hidden="true">
          <circle cx="8" cy="8" r="7" fill="none" stroke="#f39c12" stroke-width="1.5"/>
          <path d="M5.6 4.6l1.2 1.3-.6 1c.5 1 1.2 1.7 2.2 2.2l1-.6 1.3 1.2-.7 1.2c-2.7-.3-5-2.6-5.3-5.3z" fill="#f39c12"/>
        </svg>
        <span>000 222 0000</span>
      </div>
      <div>2847 West Linden Ave.,</div>
      <div>Suite 310 Anaheim, CA 92806</div>
    </div>
  </section>

  <section class="card card-back">
    <div class="appointment">
      <p class="appointment-line">YOUR NEXT APPOINTMENT <span class="fill">....................... at................ am/pm</span></p>
      <div class="days">
        <span class="day"><span class="day-box"></span>MON</span>
        <span class="day"><span class="day-box"></span>TUE</span>
        <span class="day"><span class="day-box"></span>WED</span>
        <span class="day"><span class="day-box"></span>THU</span>
        <span class="day"><span class="day-box"></span>FRI</span>
        <span class="day"><span class="day-box"></span>SAT</span>
      </div>
    </div>
    <div class="notice-band">If unable to keep appointment, kindly give 24hrs notice.</div>
    <div class="website">www.<span class="domain">lanternbaydental</span>.com</div>
  </section>

</body>
</html>
```